Travesco Business Cards

We need a business card design for Travesco Mining.

This is a B2B company that buys and sells large machinery tires within the coal mining industry. The design should the strong, crisp and masculine. I have uploaded the company logo and rough mock-up of what the back of the card should look like. the front of the card should have the same look/feel as the back. I need editable templates for both the front and the back of the card.

Color scheme should be grey/green/black

Contact information to include on the card:
Name: Dale Pemberton
Title: Managing Director
Phone: 214-503-6192
Address: 1185 Wexley #3 Dallas, TX 75211
Email: Dale@Travesco-example.com

I am also opening a contest for letterhead design. If you submit a business card design, please also submit a letterhead design with the same look/feel. The winner of the business card design will also will the letter head and be paid for both.

Target Market(s)

Procurement men/women in the coal mining industry

Industry/Entity Type

Coal Mining

```html
<!DOCTYPE html>
<html lang="en">
<head>
<meta charset="utf-8">
<title>Travesco Mining – Business Cards</title>
<link rel="stylesheet" href="https://fonts.googleapis.com/css2?family=Montserrat:wght@700&family=Questrial&display=swap">
<style>
  :root {
    --canvas: #e9e9ec;
    --card-white: #f7f8f8;
    --charcoal: #4f5356;
    --green: #3ea30a;
    --ink: #3b3e40;
    --muted: #5a5e61;
  }
  * { box-sizing: border-box; margin: 0; padding: 0; }
  html, body { width: 1200px; height: 934px; overflow: hidden; }
  body {
    background: var(--canvas);
    position: relative;
    font-family: "Questrial", sans-serif;
    color: var(--ink);
  }
  .card {
    position: absolute;
    width: 500px;
    height: 286px;
    border-radius: 3px;
    overflow: hidden;
    box-shadow: 0 10px 28px rgba(0,0,0,.14);
  }
  .card--back { left: 80px; top: 170px; background: var(--charcoal); }
  .card--front { left: 620px; top: 450px; background: var(--card-white); }

  .wordmark {
    position: absolute;
    display: flex;
    align-items: center;
    gap: 10px;
    font-family: "Montserrat", sans-serif;
    font-weight: 700;
    letter-spacing: .06em;
    text-transform: uppercase;
    white-space: nowrap;
  }
  .wordmark__square { width: 16px; height: 16px; background: var(--green); flex: none; }
  .card--back .wordmark { left: 130px; top: 128px; font-size: 26px; color: #ffffff; }
  .card--front .wordmark { right: 30px; top: 34px; font-size: 22px; color: var(--ink); }

  .bands { position: absolute; left: 0; bottom: 0; width: 500px; height: 60px; }

  .person { position: absolute; left: 34px; top: 178px; }
  .person__name {
    font-family: "Montserrat", sans-serif;
    font-weight: 700;
    font-size: 15px;
    letter-spacing: .03em;
    text-transform: uppercase;
    color: var(--ink);
  }
  .person__title { font-size: 12px; color: var(--muted); margin-top: 4px; }

  .contact { position: absolute; left: 246px; top: 108px; font-size: 11.5px; color: var(--muted); }
  .contact__row { display: flex; align-items: center; gap: 7px; margin-bottom: 6px; }
  .contact__icon { width: 14px; height: 14px; flex: none; }

  .address { position: absolute; right: 26px; top: 92px; font-size: 11.5px; line-height: 1.55; color: var(--muted); text-align: left; }
</style>
</head>
<body>

  <section class="card card--back" aria-label="Card back">
    <div class="wordmark"><span class="wordmark__square"></span>Travesco Mining</div>
  </section>

  <section class="card card--front" aria-label="Card front">
    <div class="wordmark"><span class="wordmark__square"></span>Travesco Mining</div>

    <div class="address">1185 Wexley #3<br>Dallas, TX 75211</div>

    <div class="contact">
      <div class="contact__row">
        <svg class="contact__icon" viewBox="0 0 14 14" aria-hidden="true">
          <circle cx="7" cy="7" r="6.3" fill="none" stroke="#3ea30a" stroke-width="1.2"/>
          <path d="M4.6 3.8l1.3 1.6-.7.9c.5 1 1.3 1.8 2.3 2.3l.9-.7 1.6 1.3-.8 1c-2.6-.4-4.9-2.7-5.3-5.3z" fill="#3ea30a"/>
        </svg>
        <span>214-503-6192</span>
      </div>
      <div class="contact__row">
        <svg class="contact__icon" viewBox="0 0 14 14" aria-hidden="true">
          <circle cx="7" cy="7" r="6.3" fill="#3ea30a"/>
          <rect x="3.6" y="4.6" width="6.8" height="4.8" fill="none" stroke="#fff" stroke-width="1"/>
          <path d="M3.8 4.9L7 7.4l3.2-2.5" fill="none" stroke="#fff" stroke-width="1"/>
        </svg>
        <span>Dale@Travesco-example.com</span>
      </div>
    </div>

    <div class="person">
      <div class="person__name">Dale Pemberton</div>
      <div class="person__title">Managing Director</div>
    </div>

    <svg class="bands" viewBox="0 0 500 60" aria-hidden="true">
      <polygon points="0,42 272,42 264,60 0,60" fill="#3ea30a"/>
      <polygon points="282,26 500,26 500,40 274,40" fill="#4f5356"/>
    </svg>
  </section>

</body>
</html>
```